Dr K.L. Fenwick, Consultant General Surgeon

Modern minimalistic look [shades of blue should be included]
I would like an interactive website which gives information about
1. Home page: office location
Medical Partners
📞(876) 555-0192-7
📱(876) 555-0147
📍42 Marigold Crescent, Kingston 10

VelaMedix
1-876-555-0163 / 1-876-555-0178 / 1-876-555-0129
📍37 North Cedar Grove RD, Kingston, Jamaica (Upstairs Brisa Linwood)
Info@velamedix.example

Beacon Care Medical Suites
📞(876) 555-0184
📱(876) 555-0136
📍Shop 22-23, Palm Crest Shopping Mall, Portmore

Corwell Medical Centre
📞 (876) 555-0151
📍 9 Pellowin Street , May Pen
The office logos will be attached
Booking details on this page or 2nd page with procedures

2. My surgical services . - I will attach a business card with the information for this section - do not upload the actual business card on the site

3. Allow the booking of appointments at any of the offices
4. A section where short explainer videos will be uploaded (this section is titled "Surgery in 3D"- I will upload an example below
5. A section- which shows videos of procedures. This section is titled "Surgical procedures" - I will upload one below
these videos will similar the same as the ones on my Instagram account
Link: https://www.instagram.com/dr_klfenwick?igsh=QmVyZXhhbXBsZQ&utm_source=qr

6. Gallery- section with pictures from interviews/ presentations/conferences etc

Each section should be on a different page.
The clearly defined sections can be represented from a HOME PAGE or drop-down menu
SIMILAR websites:
Modern professional design style (fonts and layout)- https://brightscalpelstudio.example
others -- this best captures the style I'm looking for. I prefer if the page is not crowded
https://velamedix.example
layered effect -- https://quillbankclinic.example/general-surgeon/
https://drpetrahalvik.example

I have updated the brief

Target Market(s)

Patients who require general surgical care

Coding

Coded - Design and coding required

Number of Pages Required

5+ page

Requirements
Must have
• Each section should be on a different page.

```html
<!DOCTYPE html>
<html lang="en">
<head>
<meta charset="utf-8">
<title>Dr K.L. Fenwick – Consultant General Surgeon</title>
<link href="https://fonts.googleapis.com/css2?family=Outfit:wght@300;400;500;600;700;800&display=swap" rel="stylesheet">
<style>
:root{
  --navy:#0d2846;
  --navy-line:#1f3d60;
  --orange:#eea04f;
  --sky:#8eabdb;
  --cream:#f8f3ee;
  --ink:#1c1c1c;
  --muted:#555;
  --white:#fff;
}
*{box-sizing:border-box;margin:0;padding:0}
html,body{width:1200px;height:4124px;overflow:hidden}
body{font-family:"Outfit",sans-serif;color:var(--ink);background:var(--white);position:relative}
section,header,footer{position:absolute;left:0;width:1200px}
.abs{position:absolute}
.btn{position:absolute;display:flex;align-items:center;justify-content:center;font-size:13px;border-radius:3px;color:var(--white);background:var(--orange)}
.btn-outline{background:transparent;border:1.5px solid var(--white)}
.photo{position:absolute}
h1,h2,h3{font-weight:700}

/* header + hero */
.site-header{top:0;height:634px;background:var(--navy);color:var(--white)}
.nav{position:absolute;top:0;left:0;width:1200px;height:53px;border-bottom:1px solid var(--navy-line)}
.brand{position:absolute;left:94px;top:13px;font-size:21px;font-weight:700}
.nav-links{position:absolute;right:94px;top:19px;display:flex;gap:26px;font-size:13px}
.hero-title{left:93px;top:238px;font-size:39px;line-height:43px;font-weight:700}
.hero-sub{left:93px;top:331px;font-size:14px}
.hero-link{left:216px;top:382px;font-size:13px}
.hero-photo{left:703px;top:99px;width:403px;height:472px;border-radius:42px;background:linear-gradient(150deg,#5d8f86,#3e8a6d 45%,#6ea690 75%,#b8c7c0)}

/* services */
.services{top:634px;height:432px;background:var(--cream)}
.section-title{width:1200px;text-align:center;font-size:37px}
.section-sub{width:1200px;text-align:center;font-size:12.5px}
.service{position:absolute;top:160px;width:178px}
.service .photo{position:relative;width:178px;height:142px;border-radius:12px}
.service h3{font-size:12px;margin:14px 0 0 7px}
.service p{font-size:11px;color:var(--muted);margin:4px 0 0 7px}

/* about */
.about{top:1066px;height:551px;background:var(--white)}
.about-panel{left:160px;top:105px;width:415px;height:446px;background:var(--sky)}
.about-portrait{left:185px;top:35px;width:393px;height:516px;border-radius:180px 180px 0 0;background:linear-gradient(180deg,#3d2b22 0 20%,#1b2430 45%,#232a35)}
.about h2{left:662px;top:130px;font-size:36px}
.about .lead{left:662px;top:186px;font-size:17px}
.about .copy{left:662px;top:213px;width:400px;font-size:12px;line-height:19px;color:#333}
.about .name{left:662px;top:296px;font-size:17px}
.about .creds{left:662px;top:323px;font-size:12px;line-height:19px;color:#333}

/* videos */
.videos{top:1617px;height:645px;background:var(--navy);color:var(--white)}
.video-card h3{position:absolute;font-size:18px;font-weight:600}
.video-card p{position:absolute;font-size:12.5px;line-height:19px}
.play{position:absolute}

/* locations */
.locations{top:2262px;height:568px;background:var(--white)}
.loc-panel{left:709px;top:0;width:491px;height:568px;background:var(--sky)}
.locations h2{left:141px;top:200px;font-size:36px;line-height:38px}
.locations .intro{left:144px;top:290px;width:340px;font-size:12.5px;line-height:19px;color:#333}
.office{position:absolute;top:144px;width:246px;height:288px;background:var(--white);border-radius:12px;overflow:hidden}
.office .photo{position:relative;width:246px;height:178px}
.office h3{font-size:12px;margin:22px 0 0 30px}
.office p{font-size:10.5px;line-height:16px;margin:6px 0 0 30px;color:#444}

/* booking */
.booking{top:2830px;height:185px;background:var(--navy);color:var(--white)}
.booking h2{left:141px;top:66px;font-size:37px}
.booking p{left:141px;top:116px;font-size:12.5px}

/* why */
.why{top:3015px;height:430px;background:var(--white)}
.reason{position:absolute;top:145px;width:240px;text-align:center}
.reason .icon{width:78px;height:78px;margin:0 auto;border-radius:10px;background:var(--sky);border:3px solid #c9d8f0;display:flex;align-items:center;justify-content:center}
.reason h3{font-size:15px;font-weight:600;margin-top:18px}
.reason p{font-size:11px;line-height:16px;color:#555;margin-top:6px}

/* contact */
.contact{top:3445px;height:450px;background:linear-gradient(90deg,#0f2d4c 0 45%,#33475a 70%,#7a6a66);color:var(--white)}
.contact h2{left:141px;top:135px;font-size:36px;line-height:38px}
.contact p{left:141px;top:232px;width:400px;font-size:12.5px;line-height:19px}
.form-panel{left:674px;top:-56px;width:394px;height:459px;border-radius:28px;background:var(--sky)}
.field{position:absolute;left:38px;width:315px;height:44px;background:var(--white);border-radius:3px;font-size:12px;color:#444;padding:15px 18px}
.submit{left:38px;top:370px;width:315px;height:45px;font-size:13px;font-weight:600}

/* footer */
.site-footer{top:3895px;height:229px;background:var(--navy);color:var(--white)}
.site-footer .brand{left:147px;top:92px}
.foot-info{left:441px;top:74px;font-size:11px;line-height:16px}
.foot-links{left:773px;top:82px;display:flex;gap:22px;font-size:13px}
.socials{left:773px;top:112px;display:flex;gap:18px}
.socials span{width:9px;height:9px;border-radius:50%;background:var(--white);display:block}
.copyright{width:1200px;top:186px;text-align:center;font-size:11px}
.to-top{left:1109px;top:164px;width:32px;height:32px;border-radius:50%;background:#1d3a5c;display:flex;align-items:center;justify-content:center}
</style>
</head>
<body>

<header class="site-header">
  <nav class="nav">
    <div class="brand">Dr K.L. Fenwick</div>
    <div class="nav-links"><span>Home</span><span>About</span><span>Services</span><span>Blog</span><span>Contact</span></div>
  </nav>
  <h1 class="abs hero-title">Dr K.L. Fenwick<br>Consultant General Surgeon</h1>
  <div class="abs hero-sub">Redefining Surgical Expertise with Compassionate Care</div>
  <div class="btn" style="left:93px;top:373px;width:108px;height:35px">Learn More</div>
  <div class="abs hero-link">Book an Appointment &nbsp;→</div>
  <div class="photo hero-photo" role="img" aria-label="Surgeon in green scrubs and cap during an operation"></div>
</header>

<section class="services">
  <h2 class="abs section-title" style="top:72px">Our Services</h2>
  <div class="abs section-sub" style="top:124px">Comprehensive Care Across Key Areas of General Surgery</div>
  <div class="service" style="left:145px"><div class="photo" role="img" aria-label="Patient touching her throat" style="background:linear-gradient(135deg,#d9c3b3,#a98c7b)"></div><h3>Thyroid Disorders</h3><p>Learn More →</p></div>
  <div class="service" style="left:328px"><div class="photo" role="img" aria-label="Hands examining a patient's abdomen" style="background:linear-gradient(135deg,#c8d6e4,#7d9dbb)"></div><h3>Laparoscopic Hernia Repair</h3><p>Learn More →</p></div>
  <div class="service" style="left:511px"><div class="photo" role="img" aria-label="Surgical team performing endoscopy" style="background:linear-gradient(135deg,#3c7f7a,#2a5d6f)"></div><h3>Endoscopy &amp; Gastroscopy</h3><p>Learn More →</p></div>
  <div class="service" style="left:694px"><div class="photo" role="img" aria-label="Doctor consulting a patient lying on a bed" style="background:linear-gradient(135deg,#e4dcd2,#b6a89a)"></div><h3>Colonoscopy</h3><p>Learn More →</p></div>
  <div class="service" style="left:877px"><div class="photo" role="img" aria-label="Surgical dressing on a patient's abdomen" style="background:linear-gradient(135deg,#c9a893,#e6dfd8)"></div><h3>Gallbladder Surgery</h3><p>Learn More →</p></div>
</section>

<section class="about">
  <div class="abs about-panel"></div>
  <div class="photo about-portrait" role="img" aria-label="Portrait of the surgeon in a dark suit and tie"></div>
  <h2 class="abs">About Us</h2>
  <div class="abs lead">Your Trusted Partner in Surgical Care</div>
  <div class="abs copy">Led by Dr K.L. Fenwick, our practice is dedicated to delivering high-quality surgical solutions backed by over 20 years of clinical expertise. We believe in providing clear, factual explanations to empower patients in making informed decisions about their health.</div>
  <div class="abs name">Dr K.L. Fenwick</div>
  <div class="abs creds">Senior Consultant General Surgeon<br>Expert in minimally invasive and open surgical techniques<br>Accredited at leading private hospitals</div>
  <div class="btn" style="left:659px;top:392px;width:108px;height:34px">Doctor's Bio</div>
</section>

<section class="videos">
  <div class="video-card">
    <div class="photo" role="img" aria-label="Surgical team operating with monitors in theatre" style="left:143px;top:97px;width:554px;height:341px;border-radius:14px;background:linear-gradient(135deg,#cfd8de,#6d93b8 55%,#2f4f6b)"></div>
    <svg class="play" style="left:392px;top:243px" width="48" height="48" viewBox="0 0 48 48"><circle cx="24" cy="24" r="24" fill="#000" fill-opacity=".45"/><path d="M19 15 L34 24 L19 33Z" fill="#fff"/></svg>
    <h3 style="left:143px;top:455px">Surgery in 3D</h3>
    <p style="left:143px;top:483px;width:420px">Explore surgical procedures through engaging 3D explainer videos, designed to simplify complex medical processes.</p>
    <div class="btn" style="left:141px;top:533px;width:108px;height:35px">Watch Now</div>
  </div>
  <div class="video-card">
    <div class="photo" role="img" aria-label="Surgeon in scrubs and cap during a procedure" style="left:709px;top:97px;width:349px;height:341px;border-radius:14px;background:linear-gradient(150deg,#6f9488,#3f8a6d 50%,#7aa899)"></div>
    <h3 style="left:709px;top:455px">Surgical Procedures</h3>
    <p style="left:709px;top:483px;width:380px">Detailed insights into various procedures through informative videos, offering a closer look at surgical practices.</p>
    <div class="btn btn-outline" style="left:709px;top:533px;width:109px;height:35px">View Videos</div>
  </div>
</section>

<section class="locations">
  <div class="abs loc-panel"></div>
  <h2 class="abs">Visit Us at<br>Convenient Locations</h2>
  <div class="abs intro">We serve patients across multiple offices, ensuring easy access to our surgical expertise.</div>
  <div class="btn" style="left:144px;top:341px;width:127px;height:35px">Get Directions</div>
  <div class="office" style="left:558px"><div class="photo" role="img" aria-label="Clinic waiting room with reception desk" style="background:linear-gradient(135deg,#e8eef3,#8ea0b0 60%,#2b2f36)"></div><h3>Medical Partners</h3><p>42 Marigold Crescent, Kingston 10<br>Tel: (876) 555-0192-7<br>Mobile: (876) 555-0147</p></div>
  <div class="office" style="left:815px"><div class="photo" role="img" aria-label="Consultation room with examination chair" style="background:linear-gradient(135deg,#f1f3f2,#a7b6b2 60%,#4c7a74)"></div><h3>VelaMedix</h3><p>37 North Cedar Grove RD, Kingston<br>Tel: 1-876-555-0163<br>Info@velamedix.example</p></div>
  <svg class="abs" style="left:982px;top:470px" width="70" height="20" viewBox="0 0 70 20" fill="none" stroke="#fff" stroke-width="1.6" stroke-linecap="round"><path d="M3 10H23M3 10L10 3M3 10L10 17"/><path d="M47 10H67M67 10L60 3M67 10L60 17"/></svg>
</section>

<section class="booking">
  <h2 class="abs">Book an Appointment</h2>
  <p class="abs">Schedule your consultation at any of our locations through our streamlined online booking system.</p>
  <div class="btn" style="left:937px;top:81px;width:126px;height:35px">Book Now</div>
</section>

<section class="why">
  <h2 class="abs section-title" style="top:77px">Why Choose Us?</h2>
  <div class="reason" style="left:202px"><div class="icon"><svg width="36" height="36" viewBox="0 0 36 36" fill="none" stroke="#fff" stroke-width="1.6"><circle cx="18" cy="16" r="10"/><circle cx="18" cy="16" r="3.5"/><path d="M14 26v6h10v-6"/></svg></div><h3>Proven Expertise</h3><p>Over two decades of experience in general surgery and advanced techniques.</p></div>
  <div class="reason" style="left:480px"><div class="icon"><svg width="36" height="36" viewBox="0 0 36 36" fill="none" stroke="#fff" stroke-width="1.6"><ellipse cx="15" cy="14" rx="11" ry="8"/><path d="M10 21l-3 6 7-4"/><path d="M22 21c4 0 9-2 9-6"/></svg></div><h3>Transparent Communication</h3><p>Clear and direct explanations for every step of your care.</p></div>
  <div class="reason" style="left:767px"><div class="icon"><svg width="36" height="36" viewBox="0 0 36 36" fill="none" stroke="#fff" stroke-width="1.6"><path d="M6 20a12 12 0 0 1 24 0"/><rect x="4" y="19" width="5" height="8" rx="2"/><rect x="27" y="19" width="5" height="8" rx="2"/><path d="M30 27c0 3-4 5-8 5"/></svg></div><h3>Comprehensive Support</h3><p>Assistance with a wide range of insurance plans and post-operative care.</p></div>
</section>

<section class="contact" role="img" aria-label="Blurred surgeon in mask as background photograph">
  <h2 class="abs">Have a health concern?<br>Contact us today.</h2>
  <p class="abs">We understand your anxieties and we're here to support you throughout your health journey. If you would like to book an appointment or seek a second opinion, reach out to us through our enquiry form or give us a call at (876) 555-0192-7</p>
  <form class="abs form-panel">
    <div class="field" style="top:78px">Name*</div>
    <div class="field" style="top:130px">Email*</div>
    <div class="field" style="top:182px">Phone*</div>
    <div class="field" style="top:234px;height:114px">Message*</div>
    <div class="btn submit">Submit Now</div>
  </form>
</section>

<footer class="site-footer">
  <div class="brand">Dr K.L. Fenwick</div>
  <div class="abs foot-info">
    <svg width="8" height="10" viewBox="0 0 8 10"><path d="M4 10C1 6 0 5 0 4a4 4 0 0 1 8 0c0 1-1 2-4 6z" fill="#fff"/></svg>
    &nbsp;42 Marigold Crescent, Kingston 10<br>
    &nbsp;&nbsp;&nbsp;&nbsp;Monday - Friday: 8:00 AM - 6:00 PM<br>
    <svg width="9" height="9" viewBox="0 0 10 10"><circle cx="5" cy="5" r="4" fill="none" stroke="#fff"/></svg>
    &nbsp;Saturday: 9:00 AM - 2:00 PM<br>
    <span style="text-decoration:underline;color:#8eabdb;font-size:10px">Get Direction</span>
  </div>
  <div class="abs foot-links"><span>Home</span><span>About</span><span>Services</span><span>Blog</span><span>Contact</span></div>
  <div class="abs socials" aria-label="Social media links"><span></span><span></span><span></span><span></span></div>
  <div class="abs copyright">©Copyright 2024 | All Rights Reserved</div>
  <div class="abs to-top"><svg width="10" height="8" viewBox="0 0 10 8"><path d="M1 6l4-4 4 4" fill="none" stroke="#fff" stroke-width="1.5"/></svg></div>
</footer>

</body>
</html>
```